Schriften der Gezeiten - Die Glockenturmfälle
Zielgruppe
Hello there, I'm a selfpublisher from germany, and i just finished a projekt. It plays 2016 in Germany, Nürnberg. And it contains all manner of typical fantasy elemants in it, but there is not one sparkling vampire. :)
Hallo erstmal, ich bin Selfpublisher und habe gerade ein Fantasy Buchprojekt beendet. Es spielt im Grunde jetzt, in Nürnberg. Es kommen allerlei typische Fantasy Elemente darin vor, was es jedoch nicht gibt sind glitzernde Vampire.
Aufgabenstellung
The Corpse of a young woman was found in an Park in Nürnberg. She was not only killed, someone took her heart and left her with Dogbitemarks, and a red cape.
Torvald is a wolfshaper, he works for the police, it is his task to find the killer.
There are all kind of fantasy persons in the story. So there is no need to put the wolf in the middle. :) I woud like to put the "Red Ridding Hood" there.
But I'm open for other suggestions.
In diesem Buch passieren ein paar wirklich ätzdende Ritualmorde, die Opfer werden alle mit einem roten Cape bedeckt oder bekleidet gefunden. Der Fall wird bearbeitet, von einem Wolfswandler in der KriPo und seiner leicht Psychopatischen "Vorgesetzten" in der Welt der Surrealen, bzw Übernatürlichen.
Was ich mir vorgestellt hatte war nicht den Wolf in den Vordergrund zu stellen, da es nicht expliziet um Werwölfe geht. Sondern viel mehr auf das Rotkäppchen einzugehen.
Das beste was mir bis jetzt einfällt wäre ein Rotkäppchen im Profil, das in der ausgestreckten Hand vor sich entweder einen Ritualdolch hält oder, dass die Hand zumindest ziehmlich Blutig wirkt und daruf ein Edelstein liegt. Das ganze im Aquarell.
Ich bin jedoch auch für komplett andere Vorschläge offen.
Wenn es noch Fragen zum Inhalt gibt könnt ihr euch gerne an mich wenden.
Ich freue mich auf die Zusammenarbeit.

```html
<!DOCTYPE html>
<html lang="de">
<head>
<meta charset="utf-8">
<title>Schriften der Gezeiten – Die Glockenturmfälle</title>
<link href="https://fonts.googleapis.com/css2?family=Arimo:wght@400;700&family=Lobster+Two&family=Montserrat:wght@800&family=Dosis:wght@300&display=swap" rel="stylesheet">
<style>
  :root {
    --ink-red: #9a3a40;
    --ink-red-dark: #7a2a30;
    --paper-white: #ffffff;
    --fog-light: #b8b8ad;
    --fog-mid: #7c7f77;
    --forest-dark: #33352f;
    --leaf-brown: #6d5d52;
    --cape-red: #8c2e38;
    --barcode-white: #fbfaf6;
  }
  * { margin: 0; padding: 0; box-sizing: border-box; }
  html, body { width: 1200px; height: 874px; overflow: hidden; background: #222; }
  .book-wrap { position: relative; width: 1200px; height: 874px; overflow: hidden; }

  .cover-art {
    position: absolute; inset: 0;
    background:
      radial-gradient(ellipse 90px 160px at 975px 590px, var(--cape-red) 0%, rgba(140,46,56,0.85) 60%, rgba(140,46,56,0) 100%),
      radial-gradient(circle 110px at 920px 130px, rgba(60,58,60,0.85) 0%, rgba(60,58,60,0.6) 70%, rgba(60,58,60,0) 100%),
      radial-gradient(ellipse 420px 260px at 930px 760px, rgba(120,100,88,0.9) 0%, rgba(109,93,82,0.5) 60%, rgba(109,93,82,0) 100%),
      linear-gradient(180deg, #8b8a80 0%, var(--fog-light) 18%, #9a9b92 32%, var(--fog-mid) 45%, var(--forest-dark) 60%, #3c3a34 75%, var(--leaf-brown) 100%);
  }

  .back-blurb {
    position: absolute; left: 64px; top: 174px; width: 410px;
    font-family: "Arimo", Arial, sans-serif; font-size: 15px; line-height: 18.2px;
    color: var(--paper-white); text-align: justify; hyphens: auto;
  }
  .back-blurb .blurb-lead { color: var(--ink-red); font-weight: 700; margin-bottom: 16px; }
  .back-blurb p + p { margin-top: 18px; }

  .barcode-area {
    position: absolute; left: 179px; top: 781px; width: 189px; height: 93px;
    background: var(--barcode-white);
  }

  .spine-title, .spine-subtitle, .spine-author {
    position: absolute; writing-mode: vertical-rl; white-space: nowrap;
  }
  .spine-title {
    left: 586px; top: 52px;
    font-family: "Lobster Two", cursive; font-size: 48px; line-height: 52px;
    color: var(--ink-red); text-shadow: 1px 1px 2px rgba(0,0,0,0.35);
  }
  .spine-subtitle {
    left: 565px; top: 116px;
    font-family: "Montserrat", sans-serif; font-weight: 800; font-size: 22px; line-height: 24px;
    letter-spacing: 1.5px; color: var(--paper-white);
  }
  .spine-author {
    left: 586px; top: 660px;
    font-family: "Dosis", sans-serif; font-weight: 300; font-size: 27px; line-height: 28px;
    color: var(--paper-white);
  }

  .front-title {
    position: absolute; left: 680px; top: 38px; width: 500px; text-align: center;
    font-family: "Lobster Two", cursive; color: var(--ink-red);
    text-shadow: 1px 2px 2px rgba(0,0,0,0.4);
  }
  .front-title .title-line { display: block; font-size: 86px; line-height: 78px; }
  .front-title .title-join { display: block; font-size: 54px; line-height: 48px; }
  .front-subtitle {
    position: absolute; left: 680px; top: 248px; width: 500px; text-align: center;
    font-family: "Montserrat", sans-serif; font-weight: 800; font-size: 24px; letter-spacing: 1.5px;
    color: var(--paper-white);
  }
  .front-author {
    position: absolute; left: 680px; top: 296px; width: 500px; text-align: center;
    font-family: "Dosis", sans-serif; font-weight: 300; font-size: 52px; letter-spacing: 1px;
    color: var(--paper-white);
  }
</style>
</head>
<body>
<div class="book-wrap">
  <div class="cover-art" role="img" aria-label="Nebliger Herbstwald mit dunklem Mond; auf laubbedecktem Weg kniet eine Gestalt im roten Kapuzenumhang mit blutigen, erhobenen Händen"></div>

  <section class="back-blurb">
    <p class="blurb-lead">Lorem ipsum dolor sit amet, consectetuer adipiscing</p>
    <p>elit. Aenean commodo ligula eget dolor. Aenean massa. Cum sociis natoque penatibus et magnis dis parturient montes, nascetur ridiculus mus. Donec quam felis, ultricies nec, pellentesque eu, pretium quis, sem. Nulla consequat massa quis enim. Donec pede justo, fringilla vel, aliquet nec, vulputate eget, arcu. In enim justo, rhoncus ut, imperdiet a, venenatis vitae, justo. Nullam dictum felis eu pede mollis pretium. Integer tincidunt.</p>
    <p>Cras dapibus. Vivamus elementum semper nisi. Aenean vulputate eleifend tellus. Aenean leo ligula, porttitor eu, consequat vitae, eleifend ac, enim. Aliquam lorem ante, dapibus in, viverra quis, feugiat a, vulputate eget, arcu. In enim justo, rhoncus ut, imperdiet a, venenatis vitae, justo. Nullam dictum felis eu pede mollis pretium. Integer tincidunt. Cras dapibus. Vivamus elementum semper nisi. Aenean vulputate eleifend tellus. Aenean leo ligula, porttitor eu, consequat vitae, eleifend ac, enim. Aliquam lorem ante, dapibus in, viverra quis, feugiat a,</p>
  </section>
  <div class="barcode-area"></div>

  <div class="spine-title">Schriften der Gezeiten</div>
  <div class="spine-subtitle">DIE GLOCKENTURMFÄLLE</div>
  <div class="spine-author">AUTOR NAME</div>

  <h1 class="front-title">
    <span class="title-line">Schriften</span>
    <span class="title-join">der</span>
    <span class="title-line">Gezeiten</span>
  </h1>
  <div class="front-subtitle">DIE GLOCKENTURMFÄLLE</div>
  <div class="front-author">AUTOR NAME</div>
</div>
</body>
</html>
```